Design our next "BOLD HORIZON" print. Size 12x36 Horizontal.

I am looking for a poster design with the text "Bold Horizon" . The print size will be a 12x36 inches.(Horizontal) It should have the American flag used throughout the design. I am looking for a very proud feeling. Font can be creative but instantly readable. The design can be old world feel and can also use the deep reds and navy blues.The image does not have to be just the flag and text. It can contain other patriotic symbols. Can also have a grungy feel. I have enclosed our last "Bold Horizon " piece for your reference. We are hoping we can get one even better. Thank You.

• Should Not be like the image example I enclosed. It's just a reference. We need something that is new and different. Plain White text.

```html
<!DOCTYPE html>
<html lang="en">
<head>
<meta charset="utf-8">
<title>Bold Horizon – Horizontal Print</title>
<link href="https://fonts.googleapis.com/css2?family=Anton&display=swap" rel="stylesheet">
<style>
  :root {
    --page: #fdfdfd;
    --navy-deep: #0b0d1a;
    --navy: #1a2466;
    --blue-light: #6f86c8;
    --rose: #d8406e;
    --red: #d81a36;
    --white-stripe: #f4eef0;
    --letter-fill: rgba(205, 208, 222, 0.48);
    --banner-shadow: rgba(20, 20, 20, 0.6);
  }
  html, body {
    margin: 0;
    padding: 0;
    width: 1200px;
    height: 1000px;
    overflow: hidden;
    background: var(--page);
  }
  .canvas {
    position: relative;
    width: 1200px;
    height: 1000px;
    background: var(--page);
  }
  .banner {
    position: absolute;
    left: 103px;
    top: 166px;
    width: 1000px;
    height: 333px;
    overflow: hidden;
    box-shadow: 8px 12px 14px var(--banner-shadow);
  }
  .flag-backdrop {
    position: absolute;
    inset: 0;
    background:
      linear-gradient(172deg, transparent 0 18%, rgba(255,255,255,0.55) 18% 27%, transparent 27% 46%, rgba(255,255,255,0.6) 46% 55%, transparent 55% 74%, rgba(255,255,255,0.55) 74% 82%, transparent 82%) right / 55% 100% no-repeat,
      linear-gradient(100deg, var(--navy-deep) 0%, var(--navy-deep) 14%, var(--navy) 26%, var(--blue-light) 42%, var(--rose) 52%, var(--red) 75%, var(--red) 100%);
  }
  .headline {
    position: absolute;
    inset: 0;
    width: 1000px;
    height: 333px;
  }
  .headline text {
    font-family: "Anton", "Oswald", sans-serif;
    fill: var(--letter-fill);
    filter: url(#letter-shadow);
  }
</style>
</head>
<body>
  <main class="canvas">
    <section class="banner">
      <div class="flag-backdrop" role="img" aria-label="Photograph of a waving American flag, stars on navy at left, red and white stripes at right"></div>
      <svg class="headline" viewBox="0 0 1000 333" xmlns="http://www.w3.org/2000/svg">
        <defs>
          <filter id="letter-shadow" x="-5%" y="-5%" width="115%" height="120%">
            <feDropShadow dx="6" dy="6" stdDeviation="3" flood-color="#000" flood-opacity="0.85"/>
          </filter>
        </defs>
        <text class="headline-top" x="262" y="164" font-size="196" textLength="470" lengthAdjust="spacingAndGlyphs">BOLD</text>
        <text class="headline-bottom" x="75" y="307" font-size="200" textLength="852" lengthAdjust="spacingAndGlyphs">HORIZON</text>
      </svg>
    </section>
  </main>
</body>
</html>
```